Kestrel Table Hour Podcast Episode Cover

I’m looking for a clean, professional, and eye-catching podcast episode cover template for my show, Kestrel Table Hour. Each week, I feature a new guest, so the design must allow me (or my team) to easily swap in a new guest’s photo without needing advanced design skills.

The template should be:

- Drag-and-drop friendly: simple for me to replace the guest’s headshot in Canva, Photoshop, or similar.
- On-brand with the Kestrel Table Hour podcast: professional yet approachable, foodservice industry-focused.
- Bold and attention-grabbing for podcast platforms and social media.

Readable text at small sizes, since covers are often viewed as thumbnails.

Design Elements to Include:

1. Podcast Title: “Kestrel Table Hour” (prominently displayed)
2. Subtitle/Space: Line for guest’s name, professional title, and company name
3. Photo Placeholder: Large, central area where I can easily drag and drop a guest photo
4. Brand Colors: attached
5. Clean, modern fonts (easy to read at thumbnail size)
6. Background graphics or patterns that give a sense of foodservice, leadership, or nationwide reach... but do not overpower the guest photo

Format Requirements:

- Editable source file (PSD, Canva template, or layered AI/INDD)
- JPG/PNG exports for immediate use
- Square format (3000x3000px) for podcast platforms

Style Inspiration:
Think modern podcast covers: bold fonts, clean lines, professional with a touch of energy.

Deliverables:

1. Final episode cover template (editable file)
2. Instructions or guidance on how to swap out guest photos

```html
<!DOCTYPE html>
<html lang="en">
<head>
<meta charset="utf-8">
<title>Kestrel Table Hour – Episode Cover</title>
<link rel="stylesheet" href="https://fonts.googleapis.com/css2?family=Bebas+Neue&family=Barlow+Condensed:wght@600;700&display=swap">
<style>
  :root {
    --navy: #1e3850;
    --gold: #f6b614;
    --white: #ffffff;
    --photo-grey: #cccccc;
  }
  html, body {
    margin: 0;
    padding: 0;
    width: 1200px;
    height: 1200px;
    overflow: hidden;
    background: var(--navy);
  }
  .episode-cover {
    display: block;
    width: 1200px;
    height: 1200px;
  }
  .show-title {
    font-family: "Bebas Neue", "Oswald", sans-serif;
  }
  .show-title--top { fill: var(--white); font-size: 322px; }
  .show-title--bottom { fill: var(--gold); font-size: 266px; }
  .accent-dot { fill: var(--gold); }
  .photo-frame { fill: var(--white); }
  .photo-slot { fill: var(--photo-grey); }
  .quote-badge__ring { fill: var(--white); }
  .quote-badge__disc { fill: var(--gold); }
  .quote-badge__mark { fill: var(--navy); }
  .guest-card { fill: var(--white); }
  .guest-text {
    font-family: "Barlow Condensed", "Arial Narrow", sans-serif;
    fill: var(--navy);
    text-anchor: end;
  }
  .guest-text--name { font-size: 58px; font-weight: 700; letter-spacing: -1px; }
  .guest-text--meta { font-size: 25px; font-weight: 600; letter-spacing: -0.5px; }
</style>
</head>
<body>
<svg class="episode-cover" viewBox="0 0 1200 1200" xmlns="http://www.w3.org/2000/svg">
  <rect width="1200" height="1200" fill="var(--navy)"/>

  <!-- Show title -->
  <text class="show-title show-title--top" x="600" y="268" text-anchor="middle" textLength="920" lengthAdjust="spacingAndGlyphs">KESTREL</text>
  <text class="show-title show-title--bottom" x="604" y="488" text-anchor="middle" textLength="1056" lengthAdjust="spacingAndGlyphs">TABLE HOUR</text>

  <!-- Horizontal accent dots -->
  <g class="dots dots--horizontal">
    <circle class="accent-dot" cx="18" cy="558" r="11"/>
    <circle class="accent-dot" cx="57" cy="558" r="11"/>
    <circle class="accent-dot" cx="95" cy="558" r="11"/>
    <circle class="accent-dot" cx="134" cy="558" r="11"/>
    <circle class="accent-dot" cx="173" cy="558" r="11"/>
    <circle class="accent-dot" cx="212" cy="558" r="11"/>
    <circle class="accent-dot" cx="250" cy="558" r="11"/>
    <circle class="accent-dot" cx="289" cy="558" r="11"/>
    <circle class="accent-dot" cx="328" cy="558" r="11"/>
  </g>

  <!-- Vertical accent dots -->
  <g class="dots dots--vertical">
    <circle class="accent-dot" cx="1134" cy="562" r="11"/>
    <circle class="accent-dot" cx="1134" cy="601" r="11"/>
    <circle class="accent-dot" cx="1134" cy="639" r="11"/>
    <circle class="accent-dot" cx="1134" cy="678" r="11"/>
    <circle class="accent-dot" cx="1134" cy="717" r="11"/>
    <circle class="accent-dot" cx="1134" cy="755" r="11"/>
    <circle class="accent-dot" cx="1134" cy="794" r="11"/>
    <circle class="accent-dot" cx="1134" cy="833" r="11"/>
    <circle class="accent-dot" cx="1134" cy="871" r="11"/>
    <circle class="accent-dot" cx="1134" cy="910" r="11"/>
    <circle class="accent-dot" cx="1134" cy="948" r="11"/>
    <circle class="accent-dot" cx="1134" cy="987" r="11"/>
    <circle class="accent-dot" cx="1134" cy="1026" r="11"/>
    <circle class="accent-dot" cx="1134" cy="1064" r="11"/>
    <circle class="accent-dot" cx="1134" cy="1103" r="11"/>
    <circle class="accent-dot" cx="1134" cy="1142" r="11"/>
    <circle class="accent-dot" cx="1134" cy="1180" r="11"/>
  </g>

  <!-- Guest photo area -->
  <path class="photo-frame" d="M307,832 A314,314 0 0 1 935,832 A314,314 0 0 1 621,1146 L307,1146 Z"/>
  <path class="photo-slot" role="img" aria-label="Guest headshot placeholder"
        d="M323,832 A298,298 0 0 1 919,832 A298,298 0 0 1 621,1130 L323,1130 Z"/>

  <!-- Quote badge -->
  <g class="quote-badge">
    <circle class="quote-badge__ring" cx="833" cy="602" r="98"/>
    <circle class="quote-badge__disc" cx="833" cy="602" r="84"/>
    <path class="quote-badge__mark" d="M784,562 h44 v34 l-30,55 h-6 l-12,-10 l20,-32 h-16 Z"/>
    <path class="quote-badge__mark" d="M840,562 h44 v34 l-30,55 h-6 l-12,-10 l20,-32 h-16 Z"/>
  </g>

  <!-- Guest details card -->
  <path class="guest-card" d="M307,1024 H600 A20,20 0 0 1 620,1044 V1146 H307 Z"/>
  <text class="guest-text guest-text--name" x="592" y="1073">Guest’s Name</text>
  <text class="guest-text guest-text--meta" x="592" y="1104">Professional Title</text>
  <text class="guest-text guest-text--meta" x="592" y="1133">Guest’s Company Name</text>
</svg>
</body>
</html>
```